Wirenexa

I'm looking to much improve our current website wirenexa.com
Updates

Low design quality

Target Market(s)

Commercial clients (Not-Residentials)

Industry/Entity Type

Office buildings and Industrial clients

Coding

Coded - Design and coding required

Number of Pages Required

5+ page

Requirements
Must have
• Very professional structured low voltage cabling projects for Wi-Fi, Audio/Video conference rooms, Access Control systems, CCTV.

```html
<!DOCTYPE html>
<html lang="en">
<head>
<meta charset="utf-8">
<title>Wirenexa – Professional Low Voltage Cabling</title>
<link href="https://fonts.googleapis.com/css2?family=Anton&family=Oswald:wght@300;400;500;600;700&family=Poppins:wght@400;500;600&display=swap" rel="stylesheet">
<style>
:root{
  --red:#d3302a;
  --red-dark:#b8231e;
  --ink:#111111;
  --white:#ffffff;
  --grey:#f1f1f1;
  --line:#9a9a9a;
  --blue-deep:#102a57;
  --blue-mid:#2f5f9e;
  --blue-light:#8fb0d8;
}
*{margin:0;padding:0;box-sizing:border-box}
html,body{width:1200px;height:4839px;overflow:hidden}
body{position:relative;background:var(--white);font-family:"Poppins",sans-serif;color:var(--ink)}
.abs{position:absolute}
.head{font-family:"Oswald",sans-serif;font-weight:600;text-transform:uppercase;line-height:1.05}
.btn{position:absolute;display:flex;align-items:center;justify-content:center;border-radius:20px;font-family:"Oswald",sans-serif;font-weight:600;font-size:11px;text-transform:uppercase;letter-spacing:.3px}
.btn-dark{background:var(--ink);color:var(--white)}
.btn-red{background:var(--red);color:var(--white);border:2px solid var(--white)}
.btn-white{background:var(--white);color:var(--ink)}
.photo{position:absolute;overflow:hidden}

/* top bar */
.topbar{left:0;top:0;width:1200px;height:36px;background:var(--red);color:var(--white);font-size:12px}
.topbar .item{position:absolute;top:9px;display:flex;align-items:center;gap:8px}
.topbar svg{width:18px;height:18px}

/* nav */
.nav{left:0;top:36px;width:1200px;height:92px;background:var(--white)}
.brand{position:absolute;display:flex;align-items:center;gap:8px;font-family:"Oswald",sans-serif;font-weight:600;color:var(--red)}
.brand .mark{background:var(--red);display:block}
.nav .menu{position:absolute;top:40px;left:537px;display:flex;gap:50px;font-family:"Oswald",sans-serif;font-size:11px;font-weight:500}
.nav .menu .active{color:var(--red)}

/* hero */
.hero{left:0;top:128px;width:1200px;height:560px;background:linear-gradient(120deg,var(--blue-deep) 0%,var(--blue-mid) 45%,var(--blue-light) 75%,#35598e 100%)}
.hero-title{left:150px;top:210px;color:var(--white)}
.hero-title .welcome{font-family:"Oswald",sans-serif;font-weight:300;font-size:58px;line-height:1.05}
.hero-title .big{font-family:"Oswald",sans-serif;font-weight:700;font-size:58px;line-height:1.05}
.hero-title .boxed{background:var(--white);color:var(--ink);padding:0 8px;margin-left:-4px}
.hero-sub{left:150px;top:404px;width:330px;color:var(--white);font-family:"Oswald",sans-serif;font-weight:500;font-size:14px;line-height:1.3}

/* about */
.about-big{left:198px;top:784px;font-family:"Anton",sans-serif;font-size:150px;line-height:.97;color:var(--ink);transform:scaleX(.78);transform-origin:left top;z-index:1}
.about-tag{left:428px;top:790px;font-family:"Oswald",sans-serif;font-weight:600;font-size:20px;line-height:1.15;z-index:3}
.about-text{left:200px;top:1094px;width:225px;font-size:11px;line-height:1.45}

/* why */
.band-black{left:0;top:1296px;width:1200px;height:41px;background:var(--ink)}
.band-red{left:0;top:1337px;width:1200px;height:265px;background:var(--red)}
.why-card{left:176px;top:1397px;width:496px;height:299px;background:var(--white);box-shadow:0 6px 18px rgba(0,0,0,.15)}
.why-title{left:749px;top:1410px;color:var(--white);font-size:46px}
.why-text{left:749px;top:1470px;width:310px;color:var(--white);font-size:12px;line-height:1.4}

/* features */
.feat-title{left:150px;top:1812px;width:415px;text-align:right;font-size:46px}
.feat-text{left:176px;top:1995px;width:390px;text-align:center;font-size:11.5px;line-height:1.45}
.red-word{color:var(--red);font-weight:600}
.comp-title{left:635px;top:2280px;font-size:46px}
.comp-text{left:635px;top:2402px;width:390px;font-size:11.5px;line-height:1.45;z-index:2}
.qual-title{left:176px;top:2632px;color:var(--white);font-size:46px}
.qual-text{left:176px;top:2762px;width:330px;color:var(--white);font-size:11.5px;line-height:1.45}

/* provide row */
.provide{left:128px;top:3232px;width:948px;height:150px;display:flex}
.provide .cell{flex:1;display:flex;flex-direction:column;align-items:center;padding-top:14px;border-right:1px solid #e4e4e4;background:linear-gradient(180deg,#fff 0%,#fbeceb 100%)}
.provide .cell:last-child{border-right:none}
.provide .icon{width:60px;height:60px;border-radius:50%;background:var(--red);display:flex;align-items:center;justify-content:center;box-shadow:0 0 0 5px #f6d2d0}
.provide .label{margin-top:12px;font-size:14px;text-align:center;line-height:1.25}
.dots{left:588px;top:3396px;display:flex;gap:6px}
.dots span{width:7px;height:7px;border-radius:50%;background:var(--red)}
.dots span+span{background:#f1a9a6}

/* services */
.serv-title{left:0;top:3475px;width:1200px;text-align:center;font-size:46px;font-weight:500}
.serv-card{position:absolute;top:3580px;width:262px;height:440px;border-radius:131px;overflow:hidden;background:#cfd7e2}
.serv-card .shade{position:absolute;left:0;right:0;bottom:0;height:200px;background:rgba(211,48,42,.92);color:var(--white);text-align:center;padding:30px 24px 0}
.serv-card h3{font-family:"Oswald",sans-serif;font-weight:600;font-size:15px;margin-bottom:10px}
.serv-card p{font-size:11px;line-height:1.4}
.serv-card .btn{position:static;margin:14px auto 0;width:110px;height:30px}

/* quote */
.quote-line{left:0;top:4188px;width:1200px;height:5px;background:var(--red)}
.quote-band{left:0;top:4193px;width:1200px;height:342px;background:var(--ink)}
.quote-title{left:608px;top:4225px;color:var(--white);font-size:46px;font-weight:500}
.field{position:absolute;color:var(--white);font-size:12px;border-bottom:1px solid #777;height:36px}
.captcha{left:733px;top:4476px;width:148px;height:34px;background:var(--white);border-radius:14px;display:flex;align-items:center;gap:8px;padding-left:12px;font-size:9px;color:#333}
.captcha i{width:13px;height:13px;border:1.5px solid #888;border-radius:2px;display:block}

/* footer */
.foot-about{left:150px;top:4650px;width:205px;font-size:11px;line-height:1.35}
.social{left:150px;top:4706px;display:flex;gap:14px}
.social span{width:40px;height:40px;border-radius:50%;background:var(--red);display:block}
.foot-col{position:absolute;top:4595px}
.foot-col h4{font-family:"Oswald",sans-serif;font-weight:600;font-size:17px;margin-bottom:14px;text-transform:uppercase}
.foot-col li{list-style:none;font-size:12px;margin-bottom:7px;display:flex;align-items:center;gap:8px}
.foot-col li::before{content:"";border-left:7px solid var(--red);border-top:4px solid transparent;border-bottom:4px solid transparent}
.foot-col.contact li::before{display:none}
.foot-col.contact li{margin-bottom:12px;align-items:flex-start}
.foot-col.contact svg{width:22px;height:22px;flex:none}
.copy{left:0;top:4807px;width:1200px;height:32px;background:var(--red);color:var(--white);font-size:10px;text-align:center;line-height:32px}
</style>
</head>
<body>

<!-- top bar -->
<div class="abs topbar">
  <div class="item" style="left:150px">
    <svg viewBox="0 0 20 20" fill="none" stroke="#fff" stroke-width="1.5"><circle cx="10" cy="10" r="9"/><rect x="5" y="6.5" width="10" height="7"/><path d="M5 7l5 4 5-4"/></svg>
    sales@wirenexa.com
  </div>
  <div class="item" style="left:335px">
    <svg viewBox="0 0 20 20" fill="none" stroke="#fff" stroke-width="1.5"><circle cx="10" cy="10" r="9"/><path d="M10 15s-4-4-4-7a4 4 0 018 0c0 3-4 7-4 7z"/><circle cx="10" cy="8" r="1.3"/></svg>
    4120 Linden Ave, Suite 310, Fairmont, VA 22030
  </div>
</div>

<!-- nav -->
<header class="abs nav">
  <div class="brand" style="left:150px;top:23px;font-size:40px;line-height:46px">
    <span class="mark" style="width:34px;height:34px"></span>Wirenexa
  </div>
  <nav class="menu"><span class="active">HOME</span><span>ABOUT US</span><span>SERVICES</span></nav>
  <div class="btn btn-dark" style="left:934px;top:30px;width:114px;height:34px">Contact us</div>
</header>

<!-- hero -->
<section class="abs hero" role="img" aria-label="Close-up photo of hands organising blue network cables in a server rack"></section>
<svg class="abs" style="left:0;top:560px" width="1200" height="130" viewBox="0 0 1200 130">
  <path d="M0 120 C220 40 420 60 600 95 C800 135 980 95 1200 10 L1200 130 L0 130Z" fill="#fff"/>
</svg>
<div class="abs hero-title">
  <div class="welcome">Welcome to</div>
  <div class="big">PROFESSIONAL</div>
  <div class="big"><span class="boxed">CABLING</span> FOR</div>
</div>
<div class="abs hero-sub">Computers, Security Cameras, Wi-Fi, VOIP Phones, Access Control, Video and Audio.</div>
<div class="btn btn-dark" style="left:150px;top:464px;width:110px;height:32px">Contact us</div>
<div class="btn btn-red" style="left:270px;top:464px;width:112px;height:32px">(888) 555-0147</div>

<!-- rotating badge -->
<svg class="abs" style="left:530px;top:578px" width="140" height="140" viewBox="0 0 140 140">
  <defs><path id="badgeRing" d="M70 70 m-52 0 a52 52 0 1 1 104 0 a52 52 0 1 1 -104 0"/></defs>
  <text font-family="Oswald, sans-serif" font-size="11" font-weight="600" letter-spacing="1.5">
    <textPath href="#badgeRing">WELCOME TO WIRENEXA <tspan fill="#d3302a">● WELCOME TO WIRENEXA ●</tspan></textPath>
  </text>
  <path d="M70 50 v34 M60 74 l10 10 10-10" stroke="#111" stroke-width="2.5" fill="none"/>
</svg>

<!-- about -->
<svg class="abs" style="left:0;top:690px" width="1200" height="606" viewBox="0 0 1200 606">
  <circle cx="560" cy="640" r="520" fill="none" stroke="#ececec" stroke-width="40"/>
  <circle cx="807" cy="287" r="225" fill="#d3302a"/>
</svg>
<div class="photo" role="img" aria-label="Photo of two smiling cabling technicians in hard hats and safety vests carrying a coil of cable" style="left:520px;top:735px;width:360px;height:561px;border-radius:170px 170px 0 0;background:linear-gradient(180deg,#f07a2c 0%,#e9e4df 35%,#c9473c 70%,#e56a2c 100%)"></div>
<div class="abs about-big">WIRE<br>NEXA</div>
<div class="abs about-tag">ELEVATE YOUR CONNECTIVITY<br>WITH WIRENEXA'S LOW VOLTAGE<br>CABLING SOLUTIONS</div>
<div class="abs about-text">Wirenexa is your premier provider of professional low voltage cabling services in Virginia, Washington DC, and Maryland. With a focus on quality, reliability, and attention to detail, we deliver exceptional cabling solutions for audio, video, security systems, computer networks, and more.</div>

<!-- why choose us -->
<div class="abs band-black"></div>
<div class="abs band-red"></div>
<svg class="abs" style="left:125px;top:1530px" width="600" height="44" viewBox="0 0 600 44">
  <circle cx="40" cy="22" r="18" fill="none" stroke="#111" stroke-width="1.5"/>
  <path d="M2 22 H60 M10 15 l-8 7 8 7" stroke="#111" stroke-width="1.5" fill="none"/>
  <circle cx="558" cy="22" r="18" fill="none" stroke="#111" stroke-width="1.5"/>
  <path d="M538 22 H598 M590 15 l8 7 -8 7" stroke="#111" stroke-width="1.5" fill="none"/>
</svg>
<div class="abs why-card">
  <div class="photo" role="img" aria-label="Photo of hands using a tablet with glowing network security icons" style="left:12px;top:12px;width:472px;height:283px;background:linear-gradient(135deg,#0c2a33 0%,#1f5c63 45%,#c4cfd4 80%,#e7ecee 100%)"></div>
  <div class="abs" style="left:12px;top:133px;width:216px;height:166px;background:var(--red);border-radius:40px 0 0 0;color:#fff">
    <svg class="abs" style="left:26px;top:64px" width="28" height="30" viewBox="0 0 28 30"><path d="M14 2 L25 6 V14 C25 21 20 26 14 28 C8 26 3 21 3 14 V6Z" fill="none" stroke="#fff" stroke-width="2"/><path d="M9 15 l4 4 7-8" fill="none" stroke="#fff" stroke-width="2"/></svg>
    <div class="abs head" style="left:22px;top:114px;font-size:16px;font-weight:500">SAFE &amp; SECURE</div>
  </div>
</div>
<div class="abs head why-title" style="font-weight:500">WHY CHOOSE US</div>
<div class="abs why-text">We are a full service cabling company and will work with your IT staff to make sure everything up and running after installation and testing.</div>
<div class="btn btn-dark" style="left:749px;top:1529px;width:114px;height:32px">Read more</div>

<!-- features -->
<svg class="abs" style="left:0;top:2320px" width="1200" height="640" viewBox="0 0 1200 640">
  <polygon points="0,5 640,253 1200,500 1200,640 0,640" fill="#d3302a"/>
</svg>
<div class="abs head feat-title" style="font-weight:500">KEY FEATURES OF<br>WIRENEXA'S CABLING<br>SERVICES:</div>
<div class="abs feat-text"><span class="red-word">Experience:</span> With years of experience in the industry, our team brings a wealth of expertise to every cabling project. Whether you're a small office or a large industrial warehouse, we have the knowledge and skills to handle jobs of any size and complexity.</div>
<div class="photo" role="img" aria-label="Photo of a technician with ear protection holding a tablet in a dark server room" style="left:635px;top:1803px;width:368px;height:437px;background:linear-gradient(180deg,#1b2634 0%,#2f3f54 40%,#6d7a3a 75%,#1c2430 100%)"></div>
<div class="abs" style="left:188px;top:2108px;width:384px;height:455px;background:#fff"></div>
<div class="photo" role="img" aria-label="Photo of a technician in a hard hat working on network cabling" style="left:197px;top:2117px;width:366px;height:437px;background:linear-gradient(160deg,#1e3c6b 0%,#3f6fa3 45%,#1b2d4f 100%)"></div>
<div class="photo" role="img" aria-label="Photo of white network cables with connectors" style="left:1040px;top:2365px;width:160px;height:450px;background:linear-gradient(200deg,rgba(255,255,255,0) 0%,#e2e4e6 40%,#c9ccd0 70%,rgba(255,255,255,0) 100%)"></div>
<div class="abs head comp-title" style="font-weight:500">COMPREHENSIVE<br>SOLUTIONS:</div>
<div class="abs comp-text">From copper CAT6 and CAT7 cabling to fiber optic installations (single and multimode) and Wi-Fi setup, we offer a full range of low voltage cabling services to meet your specific needs. Our solutions are tailored to your requirements, ensuring seamless connectivity and optimal performance.</div>

<div class="abs head qual-title" style="font-weight:500">QUALITY<br>WORKMANSHIP:</div>
<div class="abs qual-text">At Wirenexa, we take pride in our work and strive for excellence in every project we undertake. Our cabling work is engineered and implemented with care and attention to detail, ensuring reliability, durability, and long-term performance.</div>
<div class="btn btn-dark" style="left:176px;top:2871px;width:114px;height:32px">Read more</div>

<div class="photo" role="img" aria-label="Photo of a technician in a blue hard hat working on a patch panel" style="left:560px;top:2635px;width:420px;height:420px;border-radius:50%;border:6px solid #fff;background:linear-gradient(150deg,#2d4e86 0%,#c7cdd6 50%,#8d949e 100%)"></div>
<div class="photo" role="img" aria-label="Photo of white multi-pair cables with coloured wires" style="left:0;top:2950px;width:460px;height:190px;background:linear-gradient(170deg,#f3f3f3 0%,#dedede 45%,#f0c07a 60%,#f2f2f2 80%,rgba(255,255,255,0) 100%)"></div>
<svg class="abs" style="left:500px;top:2780px" width="560" height="380" viewBox="500 2780 560 380">
  <defs><path id="provideArc" d="M1018 2805 A252 252 0 0 1 690 3083"/></defs>
  <path d="M540 2950 C560 3060 640 3125 735 3135" fill="none" stroke="#8a8a8a" stroke-width="3"/>
  <path d="M722 3124 l15 11 -16 10" fill="none" stroke="#8a8a8a" stroke-width="3"/>
  <text font-family="Oswald, sans-serif" font-size="44" font-weight="600" fill="#111"><textPath href="#provideArc" startOffset="34%">What we provide</textPath></text>
</svg>

<!-- provide row -->
<div class="abs provide">
  <div class="cell"><div class="icon"><svg width="30" height="30" viewBox="0 0 30 30" fill="none" stroke="#fff" stroke-width="2"><rect x="4" y="8" width="22" height="14" rx="2"/><path d="M8 13h4M8 17h10M20 13h2"/></svg></div><div class="label">Voice &amp; Data Cable<br>Installations</div></div>
  <div class="cell"><div class="icon"><svg width="30" height="30" viewBox="0 0 30 30" fill="none" stroke="#fff" stroke-width="2"><path d="M3 15h8M11 10h10v10H11zM21 12h5M21 18h5M14 13v4M18 13v4"/></svg></div><div class="label">Copper Cable CAT6<br>and CAT7</div></div>
  <div class="cell"><div class="icon"><svg width="30" height="30" viewBox="0 0 30 30" fill="none" stroke="#fff" stroke-width="2"><rect x="9" y="10" width="5" height="14"/><rect x="17" y="10" width="5" height="14"/><path d="M11.5 10V4M19.5 10V4"/></svg></div><div class="label">Fiber Cable Single &amp;<br>Multi Mode</div></div>
  <div class="cell"><div class="icon"><svg width="30" height="30" viewBox="0 0 30 30" fill="none" stroke="#fff" stroke-width="2"><path d="M4 15L15 5l11 10M7 13v12h16V13"/><circle cx="15" cy="18" r="3"/></svg></div><div class="label">Conduit<br>Installations</div></div>
  <div class="cell"><div class="icon"><svg width="30" height="30" viewBox="0 0 30 30" fill="none" stroke="#fff" stroke-width="2"><rect x="7" y="5" width="16" height="20" rx="2"/><path d="M11 10h8M11 14h8M11 18h4"/></svg></div><div class="label">IDF and MDF<br>Installations</div></div>
</div>
<div class="abs dots"><span></span><span></span></div>

<!-- services -->
<div class="abs head serv-title">OUR SERVICES</div>
<div class="serv-card" style="left:188px">
  <div class="photo" role="img" aria-label="Photo of a modern house exterior at dusk" style="inset:0;background:linear-gradient(180deg,#7fa3c9 0%,#d9c6a8 45%,#5a4a3c 100%)"></div>
  <div class="shade"><h3>RESIDENTIAL SERVICES</h3><p>Smart home cabling and Wi-Fi system for all your devices and security.</p><div class="btn btn-white">Contact us</div></div>
</div>
<div class="serv-card" style="left:469px">
  <div class="photo" role="img" aria-label="Photo of a modern glass office building" style="inset:0;background:linear-gradient(180deg,#a9c3dd 0%,#dfe3e6 40%,#59636e 100%)"></div>
  <div class="shade" style="background:rgba(255,255,255,.9);color:#111"><h3>COMMERCIAL SERVICES</h3><p>Complete office low voltage cabling and Wi-Fi for your network and security system.</p><div class="btn btn-red" style="border:none">Contact us</div></div>
</div>
<div class="abs" style="left:468px;top:3580px;width:76px;height:76px;border-radius:50%;background:var(--red);border:4px solid #fff;display:flex;align-items:center;justify-content:center">
  <svg width="34" height="34" viewBox="0 0 30 30" fill="none" stroke="#fff" stroke-width="2"><rect x="5" y="5" width="20" height="20" rx="2"/><path d="M9 11h12M9 15h12M9 19h7"/></svg>
</div>
<div class="serv-card" style="left:751px">
  <div class="photo" role="img" aria-label="Photo of an industrial facility interior with steel structures" style="inset:0;background:linear-gradient(180deg,#6f7f93 0%,#b8c2cc 45%,#3c4652 100%)"></div>
  <div class="shade"><h3>INDUSTRIAL SERVICES</h3><p>Structured cabling, IDF and MDF for warehouses, manufacturing facilities and others.</p><div class="btn btn-white">Contact us</div></div>
</div>

<!-- quote -->
<div class="abs quote-line"></div>
<div class="abs quote-band"></div>
<div class="photo" role="img" aria-label="Photo of a smiling customer support agent with a headset" style="left:148px;top:4080px;width:410px;height:410px;border-radius:50%;border:6px solid #fff;background:linear-gradient(160deg,#e9e7e4 0%,#cdbfae 45%,#f1f1f1 100%)"></div>
<div class="abs head quote-title">REQUEST A QUOTE</div>
<div class="field" style="left:610px;top:4300px;width:190px">Name</div>
<div class="field" style="left:824px;top:4300px;width:202px">Email</div>
<div class="field" style="left:610px;top:4355px;width:416px">Phone</div>
<div class="field" style="left:610px;top:4410px;width:416px">Message</div>
<div class="btn btn-white" style="left:612px;top:4478px;width:110px;height:32px">Submit</div>
<div class="abs captcha"><i></i>I'm not a robot</div>

<!-- footer -->
<div class="brand" style="left:150px;top:4590px;font-size:40px;line-height:46px">
  <span class="mark" style="width:34px;height:34px"></span>Wirenexa
</div>
<div class="abs foot-about">Wirenexa is a local group of IT professionals, dedicated to fast, reliable and honest service.</div>
<div class="abs social"><span></span><span></span><span></span><span></span></div>

<div class="foot-col" style="left:458px">
  <h4>Request a quote</h4>
  <ul><li>Home</li><li>About Us</li><li>Services</li><li>Contact Us</li></ul>
</div>
<div class="foot-col contact" style="left:680px">
  <h4>Contact us</h4>
  <ul>
    <li><svg viewBox="0 0 22 22" fill="none" stroke="#d3302a" stroke-width="1.5"><path d="M6 3l3 4-2 2c1 2 3 4 5 5l2-2 4 3-2 3c-6 0-12-6-12-12z"/></svg>703-555-0182</li>
    <li><svg viewBox="0 0 22 22" fill="none" stroke="#d3302a" stroke-width="1.5"><circle cx="11" cy="11" r="9"/><path d="M8 6l2 3-1 1c1 1 2 2 3 2l1-1 3 2-1 2c-4 0-8-4-8-8z"/></svg>(888) 555-0147</li>
    <li><svg viewBox="0 0 22 22" fill="none" stroke="#d3302a" stroke-width="1.5"><circle cx="11" cy="11" r="9"/><rect x="6" y="7.5" width="10" height="7"/><path d="M6 8l5 4 5-4"/></svg>sales@wirenexa.com</li>
    <li><svg viewBox="0 0 22 22" fill="none" stroke="#d3302a" stroke-width="1.5"><circle cx="11" cy="11" r="9"/><path d="M11 16s-4-4-4-7a4 4 0 018 0c0 3-4 7-4 7z"/></svg>4120 Linden Ave, Suite 310<br>Fairmont, VA 22030</li>
  </ul>
</div>
<div class="abs" aria-hidden="true" style="left:928px;top:4596px;width:112px;height:112px;border-radius:50%;background:var(--grey)"></div>

<div class="abs copy">Copyright © 2010-2026 Wirenexa Company LLC. All rights reserved.</div>

</body>
</html>
```